Business Card Design

My business will be called TB Joinery & Renovations. I am a liscenced carpentar who specialises in renovations/alterations/refurbishments and maintenance. I have experience in all types of Carpentry tho. I also have experience in tiling, painting and concrete which obviously gives me an edge in the refurbishment market for building. But i am not liscenced in these trades. I pride myself on being an honest and very reliable. There are alot of tradesman where i live who are not reliable so i really want to let the community know they can trust me and that i am willing to do all types of work.
I would like to see design and is not over the top but uses earthy/modern colours which presents a down to earth message.

I would really like to communicate diversity, reliabilty and quality work.

I have attached a couple of concepts i have come up with PaperKite, These may aid you.

Industry/Entity Type

Painting

Contact Information for Business Card

Name: Dean Wolworth
Email: dean.wolw@postlark.net
Ph: 0418529364

Requirements
Must have
• Licence No: 318827K

```html
<!DOCTYPE html>
<html lang="en">
<head>
<meta charset="utf-8">
<title>TB Joinery &amp; Renovations – Business Card</title>
<link href="https://fonts.googleapis.com/css2?family=Alfa+Slab+One&family=Marcellus+SC&family=Oswald:wght@700&display=swap" rel="stylesheet">
<style>
  :root {
    --backdrop: #e8e4de;
    --card-light: #f0f0f0;
    --card-dark: #3a3a3a;
    --card-dark-deep: #2b2b2b;
    --accent: #f6e21c;
    --accent-deep: #f2c200;
    --ink: #3b3b3b;
    --ink-soft: #2a2a2a;
    --band: #e4e4e4;
  }
  * { margin: 0; padding: 0; box-sizing: border-box; }
  html, body { width: 1200px; height: 1200px; overflow: hidden; background: var(--backdrop); }
  .canvas { position: relative; width: 1200px; height: 1200px; }
  .card-shapes { position: absolute; inset: 0; }

  .front-text { position: absolute; left: 115px; width: 477px; text-align: center; color: var(--ink); }
  .owner-name {
    top: 350px; font-family: "Alfa Slab One", serif; font-size: 23px;
    color: var(--accent); text-shadow: 0 0 1px var(--ink-soft), 1px 1px 0 var(--ink-soft), -1px -1px 0 var(--ink-soft), 1px -1px 0 var(--ink-soft), -1px 1px 0 var(--ink-soft);
  }
  .trade-line {
    font-family: "Marcellus SC", serif; font-size: 19px; letter-spacing: 2px; line-height: 29px;
  }
  .trade-title { top: 382px; }
  .service-list { top: 463px; font-size: 21px; line-height: 29px; }
  .contact-list {
    top: 600px; font-family: "Marcellus SC", serif; font-size: 19px; letter-spacing: 2px;
    line-height: 25px; list-style: none;
  }
  .contact-list li { display: flex; align-items: center; justify-content: center; gap: 8px; }
  .contact-list li:first-child { font-size: 21px; }
  .contact-list .licence { font-size: 16px; margin-top: 4px; }
  .contact-icon { width: 12px; height: 12px; }

  .brand-name {
    position: absolute; font-family: "Oswald", sans-serif; font-weight: 700;
    text-align: center; line-height: 1; text-transform: uppercase;
  }
  .brand-name .brand-main { display: block; font-size: 92px; letter-spacing: 1px; }
  .brand-name .brand-sub { display: block; font-size: 31px; letter-spacing: 1px; margin-top: 8px; }
  .brand-front { left: 115px; width: 477px; top: 760px; color: var(--ink); }
  .brand-back { left: 627px; width: 477px; top: 440px; color: var(--accent); }

  .back-email {
    position: absolute; left: 627px; width: 477px; top: 812px; text-align: center;
    font-family: "Marcellus SC", serif; font-size: 22px; letter-spacing: 2px; color: var(--ink-soft);
  }
</style>
</head>
<body>
<main class="canvas">
  <svg class="card-shapes" width="1200" height="1200" viewBox="0 0 1200 1200" aria-hidden="true">
    <defs>
      <linearGradient id="tab-fill" x1="0" y1="0" x2="1" y2="0">
        <stop offset="0" stop-color="var(--accent)"/>
        <stop offset="1" stop-color="var(--accent-deep)"/>
      </linearGradient>
      <radialGradient id="dark-fill" cx="0.5" cy="0.45" r="0.7">
        <stop offset="0" stop-color="var(--card-dark)"/>
        <stop offset="1" stop-color="var(--card-dark-deep)"/>
      </radialGradient>
    </defs>

    <!-- front card -->
    <path class="tab" d="M432,218 V200 Q432,188 444,188 H556 Q570,188 570,202 V218 Z" fill="url(#tab-fill)"/>
    <path class="card-front" d="M147,181 H418 Q432,181 432,195 V216 H560 Q592,216 592,248 V986 Q592,1018 560,1018 H147 Q115,1018 115,986 V213 Q115,181 147,181 Z" fill="var(--card-light)"/>

    <!-- back card -->
    <path class="tab" d="M634,218 V200 Q634,188 646,188 H770 Q782,188 782,200 V218 Z" fill="url(#tab-fill)"/>
    <path class="card-back" d="M801,173 H1072 Q1104,173 1104,205 V981 Q1104,1013 1072,1013 H659 Q627,1013 627,981 V248 Q627,216 659,216 H773 Q787,216 787,202 V187 Q787,173 801,173 Z" fill="url(#dark-fill)"/>
    <rect class="band-rule" x="627" y="785" width="477" height="5" fill="var(--accent)"/>
    <rect class="band" x="627" y="794" width="477" height="70" fill="var(--band)"/>
    <rect class="band-rule" x="627" y="868" width="477" height="5" fill="var(--accent)"/>
  </svg>

  <p class="front-text owner-name">Dean Wolworth</p>
  <p class="front-text trade-line trade-title">Carpentry &amp;<br>All Building Services</p>
  <p class="front-text trade-line service-list">Renovations<br>Maintenance<br>General Repairs</p>
  <ul class="front-text contact-list">
    <li>
      <svg class="contact-icon" viewBox="0 0 12 12" aria-hidden="true"><circle cx="6" cy="6" r="6" fill="var(--accent)"/><path d="M3.6,3 L5,3 L5.5,4.6 L4.7,5.2 Q5.3,6.6 6.8,7.3 L7.4,6.5 L9,7 V8.4 Q5,9 3.6,3 Z" fill="var(--ink)"/></svg>
      0418529364
    </li>
    <li>
      <svg class="contact-icon" viewBox="0 0 12 12" aria-hidden="true"><circle cx="6" cy="6" r="4.8" fill="none" stroke="var(--accent)" stroke-width="2"/></svg>
      dean.wolw@postlark.net
    </li>
    <li class="licence">Licence No: 318827K</li>
  </ul>

  <p class="brand-name brand-front"><span class="brand-main">TB Joinery</span><span class="brand-sub">&amp; Renovations</span></p>
  <p class="brand-name brand-back"><span class="brand-main">TB Joinery</span><span class="brand-sub">&amp; Renovations</span></p>

  <p class="back-email">dean.wolw@postlark.net</p>
</main>
</body>
</html>
```